Web Design

Looking for web designer for total service. We would like to make it in English and Japanese for now. Also need to make Tablet version. Our website is www.brindlecove.com and www.quartzmeadow .com

```html
<!DOCTYPE html>
<html lang="ja">
<head>
<meta charset="utf-8">
<title>Quartz Meadow</title>
<link rel="stylesheet" href="https://fonts.googleapis.com/css2?family=Bebas+Neue&family=M+PLUS+1+Code:wght@400&family=Noto+Sans+JP:wght@400&display=swap">
<style>
  :root {
    --ink: #1c1c1c;
    --brown: #5b3519;
    --white: #ffffff;
    --footer: #0d0d0d;
    --logo-panel: rgba(236, 236, 236, 0.93);
    --hero-dark: #3c3e3d;
    --hero-mid: #6f6f6b;
    --rice: #d9d2c4;
    --toast: #a88a5c;
  }
  * { box-sizing: border-box; margin: 0; padding: 0; }
  html, body { width: 1047px; height: 1200px; overflow: hidden; background: var(--white); }
  .page { position: relative; width: 1047px; height: 1200px; }

  .hero {
    position: absolute; left: 0; top: 0; width: 1047px; height: 510px;
    background:
      radial-gradient(ellipse 260px 210px at 600px 320px, var(--rice) 0%, var(--toast) 45%, rgba(90,90,86,0) 100%),
      linear-gradient(160deg, #8c8c88 0%, var(--hero-mid) 35%, var(--hero-dark) 100%);
  }
  .nav {
    position: absolute; top: 36px; left: 0; width: 1047px; height: 26px;
    font-family: "Noto Sans JP", sans-serif; font-size: 18px; color: var(--white);
  }
  .nav-item { position: absolute; top: 0; white-space: nowrap; }
  .lang { position: absolute; top: 0; left: 851px; white-space: nowrap; }
  .lang .en { font-family: "Bebas Neue", sans-serif; font-size: 19px; }

  .brand-panel {
    position: absolute; left: 90px; top: 149px; width: 271px; height: 231px;
    background: var(--logo-panel);
    clip-path: polygon(0 0, 199px 0, 271px 71px, 271px 231px, 0 231px);
    display: flex; flex-direction: column; justify-content: center; align-items: center;
  }
  .brand-name {
    font-family: "Bebas Neue", sans-serif; font-size: 46px; line-height: 0.95;
    color: var(--brown); text-align: center; letter-spacing: 3px;
  }

  .intro-title {
    position: absolute; left: 90px; top: 620px;
    font-family: "Bebas Neue", sans-serif; font-size: 25px; color: var(--brown);
  }
  .copy {
    position: absolute; font-family: "M PLUS 1 Code", monospace;
    font-size: 17.5px; line-height: 23px; color: var(--ink);
  }
  .copy-intro { left: 90px; top: 655px; width: 275px; }
  .copy-service { left: 669px; top: 847px; width: 245px; }

  .photo { position: absolute; }
  .photo-desserts {
    left: 89px; top: 799px; width: 559px; height: 272px;
    background: linear-gradient(120deg, #7a3b1f 0%, #e9a23a 40%, #f4e3c9 60%, #f0a1a0 85%, #f4f1ec 100%);
  }
  .photo-cupcakes {
    left: 388px; top: 565px; width: 556px; height: 268px;
    background: linear-gradient(135deg, #9ec67a 0%, #e24a4a 30%, #f2e2d6 55%, #e3545b 80%, #c9d9a0 100%);
  }

  .footer {
    position: absolute; left: 0; top: 1119px; width: 1047px; height: 81px;
    background: var(--footer); color: var(--white);
  }
  .footer-copy {
    position: absolute; left: 92px; top: 31px;
    font-family: "Bebas Neue", sans-serif; font-size: 17px; letter-spacing: 0.2px;
  }
  .footer-lang {
    position: absolute; left: 485px; top: 29px;
    font-family: "Noto Sans JP", sans-serif; font-size: 15px;
  }
  .footer-lang .en { font-family: "Bebas Neue", sans-serif; font-size: 16px; }
  .social {
    position: absolute; left: 920px; top: 29px; width: 24px; height: 24px;
    background: #2a2a2a;
  }
</style>
</head>
<body>
<div class="page">
  <header class="hero" role="img" aria-label="Photo of grilled rice balls on a dark lacquer tray">
  </header>
  <nav class="nav">
    <span class="nav-item" style="left:90px">ホーム</span>
    <span class="nav-item" style="left:179px">事業案内</span>
    <span class="nav-item" style="left:298px">会社概要</span>
    <span class="nav-item" style="left:421px">取引先</span>
    <span class="nav-item" style="left:532px">お問合せ</span>
    <span class="nav-item" style="left:650px">求人案内</span>
    <span class="lang">日本語 | <span class="en">ENG</span></span>
  </nav>
  <div class="brand-panel">
    <div class="brand-name">QUARTZ<br>MEADOW</div>
  </div>

  <h2 class="intro-title">RELY ON BUSINESS EXPERTS IN HAWAII</h2>
  <p class="copy copy-intro">ハワイ州ホノルルを拠点に「Made in Hawaii」をコンセプトに地元企業とともにモノづくりに取り組んでいます</p>

  <div class="photo photo-desserts" role="img" aria-label="Photo of mango, strawberry and chocolate pudding cups"></div>
  <div class="photo photo-cupcakes" role="img" aria-label="Photo of flower-frosted cupcakes in a clear tray"></div>

  <p class="copy copy-service">ハワイ特産食品、加工品の製造販売をはじめ、おにぎりやデザートのケータリングを行っています</p>

  <footer class="footer">
    <span class="footer-copy">© 2017 QUARTZ MEADOW ALL RIGHTS RESERVED.</span>
    <span class="footer-lang">日本語 | <span class="en">ENG</span></span>
    <span class="social" aria-label="Social media link"></span>
  </footer>
</div>
</body>
</html>
```